Business card design needed

I would like a one sided black business card with the information provided above. Refer to my website www.brightvolleyracquet.com.au for an example of colors I have used for my site, would like to keep this consistent for my business cards also, I will upload my logo below.

I am a new small business that provides tennis customers with racquet re stringing, tennis strings and accessories.

Industry/Entity Type

Small Business

Contact Information for Business Card

Bright Volley Racquet

Derek Fenwick
Managing Director

brightvolleyracquet@mailnest.com
www.brightvolleyracquet.com.au
0471 629 305

Racquet Restringing/Tennis Strings/Accessories

Requirements
Must have
• Must have my logo and card must be black

```html
<!DOCTYPE html>
<html lang="en">
<head>
<meta charset="utf-8">
<title>Bright Volley Racquet – Business Card</title>
<link rel="stylesheet" href="https://fonts.googleapis.com/css2?family=Aldrich&display=swap">
<style>
  :root {
    --card-black: #050505;
    --lime: #b6d334;
    --ink: #161616;
    --white: #ffffff;
    --backdrop: #e9e7e4;
  }
  * { margin: 0; padding: 0; box-sizing: border-box; }
  html, body {
    width: 1200px;
    height: 475px;
    overflow: hidden;
    background: var(--backdrop);
    font-family: "Aldrich", "Arial", sans-serif;
  }
  .canvas {
    position: relative;
    width: 1200px;
    height: 475px;
  }
  .card {
    position: absolute;
    top: 81px;
    width: 548px;
    height: 312px;
    border-radius: 14px;
    overflow: hidden;
    background: var(--card-black);
  }
  .card--front { left: 38px; }
  .card--back { left: 605px; top: 85px; }

  .card__panels {
    position: absolute;
    inset: 0;
    width: 100%;
    height: 100%;
  }
  .card__panel-green { fill: var(--lime); }
  .card__rule { stroke: var(--white); stroke-width: 2; fill: none; }

  .brand-name {
    position: absolute;
    color: var(--lime);
    white-space: nowrap;
    letter-spacing: 0.01em;
  }
  .card--front .brand-name {
    left: 28px;
    top: 78px;
    font-size: 21px;
  }
  .card--back .brand-name {
    left: 0;
    right: 0;
    top: 118px;
    text-align: center;
    font-size: 31px;
  }

  .contact {
    position: absolute;
    right: 40px;
    top: 164px;
    text-align: right;
    color: var(--ink);
  }
  .contact__name {
    font-size: 19px;
    text-transform: uppercase;
    letter-spacing: 0.01em;
    line-height: 22px;
  }
  .contact__role {
    font-size: 13px;
    line-height: 18px;
    margin-bottom: 17px;
  }
  .contact__list { list-style: none; }
  .contact__item {
    font-size: 13.5px;
    line-height: 19.5px;
    display: flex;
    justify-content: flex-end;
    align-items: center;
    gap: 6px;
  }
  .contact__icon {
    width: 11px;
    height: 11px;
    fill: none;
    stroke: #3a4a12;
    stroke-width: 1.4;
  }
  .card__web {
    position: absolute;
    left: 0;
    right: 0;
    top: 240px;
    text-align: center;
    color: var(--white);
    font-size: 14px;
    letter-spacing: 0.12em;
  }
</style>
</head>
<body>
<main class="canvas">

  <section class="card card--front" aria-label="Business card front">
    <svg class="card__panels" viewBox="0 0 548 312" preserveAspectRatio="none" aria-hidden="true">
      <polygon class="card__panel-green" points="373,0 548,0 548,312 147,312"/>
      <line class="card__rule" x1="397" y1="0" x2="170" y2="312"/>
      <line class="card__rule" x1="306" y1="125" x2="548" y2="125"/>
    </svg>

    <div class="brand-name">Bright Volley Racquet</div>

    <div class="contact">
      <p class="contact__name">Derek Fenwick</p>
      <p class="contact__role">Managing Director</p>
      <ul class="contact__list">
        <li class="contact__item">
          <svg class="contact__icon" viewBox="0 0 12 12" aria-hidden="true"><path d="M3 1.5 L4.6 4 L3.6 5 Q4.6 7.4 7 8.4 L8 7.4 L10.5 9 L9.5 10.5 Q4 10 1.5 2.5 Z"/></svg>
          <span>0471 629 305</span>
        </li>
        <li class="contact__item">
          <svg class="contact__icon" viewBox="0 0 12 12" aria-hidden="true"><rect x="1" y="2.5" width="10" height="7" rx="1"/><path d="M1 3 L6 7 L11 3"/></svg>
          <span>brightvolleyracquet@mailnest.com</span>
        </li>
        <li class="contact__item">
          <svg class="contact__icon" viewBox="0 0 12 12" aria-hidden="true"><circle cx="6" cy="6" r="5"/><ellipse cx="6" cy="6" rx="2.2" ry="5"/><path d="M1 6 H11"/></svg>
          <span>www.brightvolleyracquet.com.au</span>
        </li>
      </ul>
    </div>
  </section>

  <section class="card card--back" aria-label="Business card back">
    <div class="brand-name">Bright Volley Racquet</div>
    <p class="card__web">www.brightvolleyracquet.com.au</p>
  </section>

</main>
</body>
</html>
```